Poster Design Project- New Years Eve

We are a fun and quirky bar in St Kilda (www.quillhouse.com.au). We need a poster designed for our New Years Eve Event- details as follows
Project: A1 poster-NYE
Name of Event: Copper Moons
Date of Event: New Years Eve: 31.12.12
Tagline: ‘What happens at Quill stays at Quill’
Time: 8pm-3am
Cost:
$105 all inclusive
-Includes a cocktail on arrival
-4 hour drink package – Basic Spirits, Premium Beer, Wine and Sparkling til 12AM
-Grazing style canapés and finger food
Early bird and group discounts (10+) available
Purchase your tickets at the bar or through the website
Dress: For Fun and Dancing
Venue information:
• Address: 47 Brambleton Lane St Kilda
• Phone: 6143 2057
• Email: info@quillhouse.com.au
• Website: www.quillhouse.com.au
• Management reserves the right to refuse entry
Images: Images need to be high resolution or vector images so clarity is not lost when the poster is blown up to this size
Poster production:
Poster needs to be created in either Adobe Illustrator or Photoshop so we can easily edit the details if they change after the contest ends
Please provide 3mm internal and external bleed
Theming:
Fun poster with elements of Las Vegas including: dice/casino element, Las Copper Moons, pretty girls, cocktails
25-40 year olds
Casino

```html
<!DOCTYPE html>
<html lang="en">
<head>
<meta charset="utf-8">
<title>Quill – New Years Eve – Copper Moons</title>
<link rel="stylesheet" href="https://fonts.googleapis.com/css2?family=Open+Sans:wght@400;600;700&family=Great+Vibes&display=swap">
<style>
  :root {
    --frame: #000000;
    --sky-deep: #0f5fae;
    --sky-mid: #1f86d4;
    --sky-light: #5cb8f0;
    --lime: #8cc63f;
    --sun: #f7c21b;
    --orange: #f39a1e;
    --magenta: #e6388f;
    --violet: #5a3f9c;
    --navy: #0b3f86;
    --panel-light: #ffffff;
    --panel-grey: #a9abae;
    --ink: #1e1e1e;
    --ink-soft: #555659;
    --white: #ffffff;
  }
  * { margin: 0; padding: 0; box-sizing: border-box; }
  html, body { width: 852px; height: 1200px; overflow: hidden; background: var(--frame); }
  body { font-family: "Open Sans", Arial, sans-serif; }

  .poster {
    position: absolute; left: 42px; top: 54px;
    width: 768px; height: 1089px; overflow: hidden;
    background: linear-gradient(180deg, var(--sky-mid), var(--sky-light) 55%, var(--sky-mid));
  }
  .poster-art { position: absolute; inset: 0; }

  .tagline {
    position: absolute; right: 12px; top: 4px;
    font-size: 28px; font-weight: 600; color: var(--white);
    text-shadow: 0 2px 3px rgba(0,0,0,.5);
  }

  .event-date { position: absolute; left: 22px; top: 288px; color: var(--white); }
  .event-date .label { font-size: 31px; font-weight: 600; letter-spacing: -0.5px; line-height: 1.1; }
  .event-date .day { font-size: 62px; font-weight: 600; line-height: 1; letter-spacing: 1px; }

  .venue-name {
    position: absolute; left: 10px; top: 420px;
    width: 410px; height: 92px; padding: 4px 22px;
    background: var(--white); border-radius: 6px;
    display: flex; flex-direction: column; justify-content: center;
  }
  .venue-name .name { font-size: 58px; font-weight: 700; color: var(--ink); line-height: 1; }
  .venue-name .address { font-size: 14px; font-weight: 700; color: var(--ink); letter-spacing: .5px; margin-top: 4px; }

  .details { position: absolute; left: 26px; top: 612px; color: var(--ink); }
  .details .time { font-size: 37px; font-weight: 700; color: var(--ink-soft); letter-spacing: -0.5px; }
  .details .cost { font-size: 30px; font-weight: 400; margin-top: 2px; }
  .inclusions { list-style: none; margin-top: 8px; }
  .inclusions li {
    position: relative; padding-left: 32px;
    font-size: 19px; line-height: 32px;
  }
  .inclusions li::before {
    content: ""; position: absolute; left: 2px; top: 9px;
    width: 14px; height: 14px; border: 2px solid var(--ink); border-radius: 50%;
    background: radial-gradient(circle, var(--ink) 3px, transparent 3.5px);
  }
  .notes { margin-top: 14px; font-size: 20px; line-height: 29px; }

  .venue-heading {
    position: absolute; left: 0; top: 936px;
    width: 374px; height: 51px; padding-left: 32px;
    background: var(--frame); border-radius: 0 6px 6px 0;
    font-size: 31px; font-weight: 400; color: var(--white); line-height: 51px;
  }

  .contact { position: absolute; left: 39px; top: 994px; color: var(--white); font-size: 18px; line-height: 30px; }

  .event-name {
    position: absolute; right: 22px; top: 1000px;
    font-family: "Great Vibes", cursive; font-size: 50px; color: var(--white);
  }
  .entry-note {
    position: absolute; right: 18px; top: 1070px;
    font-size: 10px; color: var(--white);
  }
</style>
</head>
<body>
<main class="poster">
  <svg class="poster-art" viewBox="0 0 768 1089" width="768" height="1089" aria-hidden="false">
    <defs>
      <linearGradient id="photoTone" x1="0" y1="0" x2="1" y2="1">
        <stop offset="0" stop-color="#3a2a24"/>
        <stop offset=".45" stop-color="#b98a6e"/>
        <stop offset="1" stop-color="#4a5a78"/>
      </linearGradient>
      <radialGradient id="panelTone" cx=".35" cy=".35" r=".8">
        <stop offset="0" stop-color="var(--panel-light)"/>
        <stop offset=".55" stop-color="#e4e5e6"/>
        <stop offset="1" stop-color="var(--panel-grey)"/>
      </radialGradient>
      <linearGradient id="footTone" x1="0" y1="0" x2="1" y2="0">
        <stop offset="0" stop-color="var(--sky-mid)"/>
        <stop offset="1" stop-color="var(--navy)"/>
      </linearGradient>
    </defs>

    <!-- background swirls -->
    <path d="M-20 120 C120 60 100 360 0 520" fill="none" stroke="var(--sky-deep)" stroke-width="40" opacity=".55"/>
    <path d="M40 0 C-10 150 30 330 60 420" fill="none" stroke="var(--white)" stroke-width="6" opacity=".35"/>
    <path d="M560 560 C700 600 760 760 700 1000" fill="none" stroke="var(--sky-deep)" stroke-width="60" opacity=".5"/>
    <path d="M620 560 C760 640 790 820 740 990" fill="none" stroke="var(--white)" stroke-width="4" opacity=".4"/>

    <!-- photo area -->
    <path d="M150 0 C100 140 150 330 280 395 C420 455 620 430 768 395 L768 0 Z"
          fill="url(#photoTone)" role="img"
          aria-label="Photo of three smiling women at a party, one holding playing cards and casino chips"/>
    <path d="M150 0 C100 140 150 330 280 395 C420 455 620 430 768 395"
          fill="none" stroke="var(--lime)" stroke-width="14"/>
    <path d="M125 0 C72 150 120 345 270 415 C420 480 640 455 768 420"
          fill="none" stroke="var(--navy)" stroke-width="10"/>

    <!-- tagline strip -->
    <path d="M156 0 L768 0 L768 48 L146 48 Z" fill="var(--white)" opacity=".28"/>

    <!-- colour band behind venue name -->
    <path d="M0 405 C250 390 500 440 768 470 L768 520 C500 480 250 445 0 450 Z" fill="var(--violet)"/>
    <path d="M0 432 C250 420 500 470 768 500 L768 560 C520 520 260 480 0 500 Z" fill="var(--sun)"/>
    <path d="M0 462 C260 455 520 500 768 530 L768 580 C520 548 270 520 0 530 Z" fill="var(--magenta)"/>
    <path d="M0 512 C260 510 520 548 768 575 L768 600 C520 572 260 540 0 545 Z" fill="var(--orange)"/>
    <path d="M0 540 C260 535 520 570 768 598" fill="none" stroke="var(--navy)" stroke-width="8"/>

    <!-- info panel -->
    <path d="M0 556 C250 548 520 570 650 610 C540 700 480 840 455 1000 L0 1000 Z" fill="url(#panelTone)"/>
    <path d="M650 610 C540 700 480 840 455 1000" fill="none" stroke="var(--lime)" stroke-width="12"/>
    <path d="M676 620 C570 710 510 850 488 1000" fill="none" stroke="var(--navy)" stroke-width="6"/>

    <!-- footer band -->
    <rect x="0" y="987" width="768" height="102" fill="url(#footTone)"/>
    <rect x="0" y="987" width="768" height="4" fill="var(--sky-light)"/>
  </svg>

  <p class="tagline">What happens at Quill stays at Quill</p>

  <div class="event-date">
    <p class="label">New Years Eve</p>
    <p class="day">31.12.12</p>
  </div>

  <div class="venue-name">
    <p class="name">Quill</p>
    <p class="address">47 BRAMBLETON LANE, ST KILDA</p>
  </div>

  <section class="details">
    <p class="time">Time: 8pm-3am</p>
    <p class="cost">Cost: $105 all inclusive</p>
    <ul class="inclusions">
      <li>Includes a cocktail on arrival</li>
      <li>4 hour drink package – Basic Spirits</li>
      <li>Premium Beer, Wine and Sparkling till 12AM</li>
      <li>Grazing style canapés and finger food</li>
    </ul>
    <p class="notes">Early bird and group discounts (10+) available<br>Purchase your tickets at the bar or through the website</p>
  </section>

  <h2 class="venue-heading">Venue information:</h2>

  <address class="contact" style="font-style: normal;">
    P: 6143 2057<br>
    E: info@quillhouse.com.au<br>
    www.quillhouse.com.au
  </address>

  <p class="event-name">Copper Moons</p>
  <p class="entry-note">Management Reserves The Right To Refuse Entry</p>
</main>
</body>
</html>
```